Modern Quillby Tree Care Website

I need a website for a full service Tree Care company. The company provides tree pruning, tree removal, tree preservation, emergency services, stump grinding, and emergency tree services.

Target Market(s)

Customers that need tree services

Industry/Entity Type

Landscaping, Tree Services

Coding

Coded - Design and coding required

Number of Pages Required

5+ page

Font styles to use
Sans Serif

Requirements
Must have
• Good clean design that showcases the services the company provides.
Nice to have
• Services page; contact form, blog, home page, about page

```html
<!DOCTYPE html>
<html lang="en">
<head>
<meta charset="utf-8">
<title>Quillby Tree Care</title>
<link rel="stylesheet" href="https://fonts.googleapis.com/css2?family=Barlow:wght@400;500;600;700&family=Roboto+Slab:wght@500;600;700&display=block">
<style>
:root{
  --cream:#f7f6dd;
  --orange:#d9801e;
  --amber:#f7a636;
  --green:#7cb83b;
  --forest:#3c5a2d;
  --footer:#2e3a21;
  --slate:#35413c;
  --ink:#2b2b26;
  --body:#4a4a42;
  --white:#ffffff;
  --slab:'Roboto Slab','Rockwell','Roboto Slab Fallback',serif;
}
*{box-sizing:border-box;margin:0;padding:0}
html,body{width:1200px;height:3505px;overflow:hidden}
body{position:relative;background:var(--cream);font-family:'Barlow',sans-serif;color:var(--body)}
.abs{position:absolute}

/* header */
.site-header{left:0;top:0;width:1200px;height:101px;background:var(--cream);border-bottom:1px solid #e4e2c0}
.brand{left:141px;top:20px;display:flex;align-items:center;gap:12px}
.brand-mark{width:50px;height:50px;background:var(--green)}
.brand-name{font-family:'Barlow',sans-serif;font-weight:700;font-size:30px;color:var(--forest);line-height:1;letter-spacing:1px;white-space:nowrap}
.header-rule{left:370px;top:68px;width:830px;height:1px;background:#e1dfbd}
.contact-email{left:645px;top:18px;text-align:right;width:200px}
.tiny-label{font-size:9px;color:#9a9a80;text-transform:uppercase;letter-spacing:.5px;white-space:nowrap}
.contact-email .value{font-size:18px;font-weight:600;color:var(--orange);white-space:nowrap}
.badge-24{left:866px;top:16px;width:38px;height:38px;border:1.5px solid var(--orange);border-radius:50%;text-align:center;color:var(--orange);font-weight:700;font-size:15px;line-height:1;padding-top:7px}
.badge-24 small{display:block;font-size:6px;font-weight:500}
.contact-phone{left:914px;top:18px}
.contact-phone .value{font-size:22px;font-weight:700;color:var(--orange);letter-spacing:.5px;white-space:nowrap}
.main-nav{left:524px;top:76px;font-family:var(--slab);font-weight:500;font-size:12px;color:#333}
.main-nav a{color:#333;text-decoration:none;position:absolute;white-space:nowrap}
.main-nav .active{background:var(--amber);color:var(--white);padding:1px 4px}

/* hero */
.hero{left:0;top:101px;width:1200px;height:586px;background:linear-gradient(120deg,#b9bfa5 0%,#7e8a5e 45%,#4f5a3a 75%,#6e6a4d 100%)}
.hero-card{left:143px;top:234px;width:426px;height:273px;background:var(--white);padding:36px 0 0 44px}
.corner{position:absolute;width:26px;height:26px}
.corner.tl{left:0;top:0;background:linear-gradient(135deg,var(--amber) 50%,transparent 50%)}
.corner.tr{right:0;top:0;background:linear-gradient(225deg,var(--amber) 50%,transparent 50%)}
.corner.bl{left:0;bottom:0;background:linear-gradient(45deg,var(--amber) 50%,transparent 50%)}
.corner.br{right:0;bottom:0;background:linear-gradient(315deg,var(--amber) 50%,transparent 50%)}
.hero-card h1{font-family:var(--slab);font-weight:600;font-size:38px;line-height:50px;color:var(--ink);white-space:nowrap}
.hero-card h1 em{font-style:normal;color:var(--orange)}
.hero-card p{margin-top:14px;font-size:17px;color:#555;white-space:nowrap}

/* about */
.about{left:0;top:687px;width:1200px;height:599px;background:linear-gradient(90deg,var(--cream) 0%,var(--cream) 55%,#e6e9c2 80%,#d9dfb2 100%)}
.about-accent{left:134px;top:791px;width:294px;height:345px;background:var(--green);clip-path:polygon(0 0,100% 0,0 100%)}
.about-photo{left:147px;top:803px;width:350px;height:375px;background:linear-gradient(160deg,#6c7c5a,#3f4a33 60%,#8a6a45)}
.eyebrow{font-size:11px;font-weight:700;letter-spacing:1.5px;color:var(--orange);text-transform:uppercase;display:flex;align-items:center;gap:8px}
.eyebrow::before,.eyebrow.center::after{content:"";width:16px;height:1.5px;background:var(--orange)}
.section-title{font-family:var(--slab);font-weight:600;color:var(--ink);line-height:1.1;white-space:nowrap}
.section-title em{font-style:normal;color:var(--green)}
.about-text{left:563px;top:800px;width:400px}
.about-text .section-title{font-size:40px;margin-top:12px}
.about-text p{font-size:14px;line-height:24px;margin-top:16px;color:#444}
.about-text p + p{margin-top:24px}
.btn{display:inline-block;font-size:11px;font-weight:700;letter-spacing:1.5px;text-transform:uppercase;text-align:center;text-decoration:none}
.btn-solid{background:var(--orange);color:var(--white)}
.about-btn{margin-top:28px;width:161px;height:37px;line-height:37px}

/* services */
.services{left:0;top:1286px;width:1200px;height:830px;background:linear-gradient(180deg,#35512a 0%,var(--forest) 40%,#3b582c 100%)}
.services-head{left:0;top:1370px;width:1200px;text-align:center}
.services-head .eyebrow{justify-content:center}
.services-head .section-title{font-size:44px;color:var(--white);margin-top:12px}
.services-head p{width:590px;margin:16px auto 0;font-size:14px;line-height:24px;color:#e6ead8}
.service-card{top:1580px;width:282px;height:329px;background:var(--white);border-radius:12px;text-align:center}
.service-card h3{height:45px;line-height:45px;background:var(--amber);border-radius:12px 12px 0 0;font-family:var(--slab);font-weight:600;font-size:17px;color:var(--white);white-space:nowrap}
.service-photo{height:163px;border-radius:0 0 14px 14px}
.service-card p{font-size:12.5px;line-height:22px;color:#777;padding:14px 24px 0}
.card-arrow{position:absolute;left:126px;bottom:-14px;width:30px;height:30px;border-radius:50%;background:var(--amber)}
.slider-arrow{top:1727px;width:38px;height:38px;border:1px solid #7f946f;border-radius:50%}
.more-services{left:520px;top:1960px;width:160px;height:37px;line-height:35px;border:1px solid var(--orange);color:var(--white)}

/* why choose */
.why{left:0;top:2116px;width:1200px;height:408px;background:linear-gradient(90deg,#5d8a35 0%,#8cb84d 25%,#a4c96a 50%,#86b548 75%,#4f7b2e 100%)}
.log-ring{left:375px;top:2075px;width:448px;height:448px;border-radius:50%;background:radial-gradient(circle,#e9d3a8 60%,#c79a63 72%,#8a5a33 78%,#6a4226 82%)}
.why-disc{left:395px;top:2095px;width:408px;height:408px;border-radius:50%;background:var(--slate);border:4px solid #f1e4c7;text-align:center;padding-top:88px}
.why-disc .eyebrow{justify-content:center}
.why-disc .section-title{font-size:36px;color:var(--white);margin-top:10px}
.why-disc ul{list-style:none;margin-top:12px}
.why-disc li{font-size:15px;font-weight:500;color:var(--white);line-height:29px}

/* contact */
.contact{left:0;top:2524px;width:1200px;height:558px;background:linear-gradient(180deg,var(--cream) 0%,#eef0cf 50%,#dfe4bb 100%)}
.contact-head{left:0;top:2640px;width:1200px;text-align:center}
.contact-head .eyebrow{justify-content:center}
.contact-head .section-title{font-size:42px;margin-top:12px}
.contact-head p{width:460px;margin:14px auto 0;font-size:14px;line-height:22px;color:#444}
.field{background:#fdfdf3;border:1px solid #dedcc0;box-shadow:0 2px 3px rgba(0,0,0,.08);font-size:11px;color:#555;padding:10px 12px}
.submit{left:895px;top:2973px;width:142px;height:36px;line-height:36px}

/* footer */
.site-footer{left:0;top:3082px;width:1200px;height:423px;background:var(--footer)}
.footer-brand{left:161px;top:3200px;display:flex;align-items:center;gap:10px}
.footer-brand .brand-name{color:#7d9a6b;font-size:21px}
.footer-about{left:161px;top:3272px;width:225px;font-size:12px;line-height:20px;color:#e6e6d6}
.footer-h{font-family:var(--slab);font-weight:600;font-size:14px;color:var(--white);text-transform:uppercase;white-space:nowrap}
.quick-links{left:464px;top:3190px}
.quick-links ul{list-style:none;margin-top:10px}
.quick-links li{font-size:12px;color:#e6e6d6;line-height:29px}
.quick-links li::before{content:"›";margin-right:6px}
.contact-info{left:626px;top:3190px;width:170px}
.ci-row{display:flex;gap:8px;font-size:12px;line-height:15px;color:#e6e6d6;margin-top:14px}
.ci-row svg{flex:none;margin-top:2px}
.socials{left:626px;top:3347px;display:flex;gap:10px}
.socials span{width:27px;height:27px;border:1.5px solid #e6e6d6;border-radius:50%}
.socials span.on{background:var(--orange);border-color:var(--orange)}
.locations{left:852px;top:3190px}
.map{left:852px;top:3229px;width:183px;height:142px;border:3px solid #7a7a6a;background:linear-gradient(135deg,#eef0ea,#dfe4df)}
.copyright{left:0;top:3467px;width:1200px;text-align:center;font-size:12.5px;color:#d8d8c6}
.copyright b{color:var(--orange)}
</style>
</head>
<body>

<header class="abs site-header">
  <div class="abs brand"><span class="brand-mark"></span><span class="brand-name">QUILLBY TREE CARE</span></div>
  <div class="abs header-rule"></div>
  <div class="abs contact-email"><div class="tiny-label">Email us</div><div class="value">info@quillbytreecare.com</div></div>
  <div class="abs badge-24">24<small>HOUR</small></div>
  <div class="abs contact-phone"><div class="tiny-label">Call Dana for a free estimate</div><div class="value">(337) 555-0148</div></div>
  <nav class="abs main-nav">
    <a class="active" style="left:0">HOME</a>
    <a style="left:81px">WHO WE ARE</a>
    <a style="left:204px">TREE CARE SERVICES</a>
    <a style="left:371px">REVIEWS</a>
    <a style="left:469px">CONTACT US</a>
  </nav>
</header>

<section class="abs hero" role="img" aria-label="Arborist in a helmet cutting a large tree limb with a chainsaw"></section>
<div class="abs hero-card">
  <span class="corner tl"></span><span class="corner tr"></span><span class="corner bl"></span><span class="corner br"></span>
  <h1>CALL <em>QUILLBY</em> FOR<br>ALL YOUR TREE<br>CARE NEEDS</h1>
  <p>Serving Lafayette and surrounding areas</p>
</div>

<section class="abs about" role="img" aria-label="Misty forest background"></section>
<div class="abs about-accent"></div>
<div class="abs about-photo" role="img" aria-label="Worker cutting a log with a chainsaw"></div>
<div class="abs about-text">
  <div class="eyebrow">Who we are</div>
  <h2 class="section-title">QUILLBY <em>TREE</em> CARE</h2>
  <p>At Quillby Tree Care, we are more than just a tree service company, we are stewards of our beautiful trees. With a passion deeply rooted in arboriculture, we embark on a mission to promote the health, beauty, and safety of your trees and landscapes.</p>
  <p>Whether it's expert tree trimming to enhance aesthetics, meticulous tree removal to mitigate hazards, or comprehensive tree health assessments to ensure safety, we approach each task with unwavering dedication and attention to detail.</p>
  <a class="btn btn-solid about-btn">More about us</a>
</div>

<section class="abs services" role="img" aria-label="Dark forest background"></section>
<div class="abs services-head">
  <div class="eyebrow center">What we do</div>
  <h2 class="section-title">OUR <em>SERVICES</em></h2>
  <p>Lorem ipsum dolor sit amet, consectetur adipisicing elit, sed do eiusmod tempor incididunt ut labore et dolore magna aliqua. Ut enim ad minim veniam, quis nostrud exercitation ullamco laboris nisi ut aliquip ex ea commodo consequat.</p>
</div>
<div class="abs slider-arrow" style="left:68px"><svg width="36" height="36"><path d="M20 13l-5 5 5 5" fill="none" stroke="#a5b596" stroke-width="1.5"/></svg></div>
<div class="abs slider-arrow" style="left:1094px"><svg width="36" height="36"><path d="M16 13l5 5-5 5" fill="none" stroke="#a5b596" stroke-width="1.5"/></svg></div>

<article class="abs service-card" style="left:136px">
  <h3>TREE GRINDING</h3>
  <div class="service-photo" role="img" aria-label="Stump grinder at work on a lawn" style="background:linear-gradient(135deg,#c9a43a,#6b6b3a 50%,#7fa05a)"></div>
  <p>Lorem ipsum dolor sit amet, consectetur adipisicing elit, sed do eiusmod tempor incididunt ut labore et dolore.</p>
  <span class="card-arrow"><svg width="30" height="30"><path d="M13 10l5 5-5 5" fill="none" stroke="#fff" stroke-width="2"/></svg></span>
</article>
<article class="abs service-card" style="left:457px">
  <h3>TREE REMOVAL</h3>
  <div class="service-photo" role="img" aria-label="Climber removing a tree against blue sky" style="background:linear-gradient(135deg,#3a7fc9,#6a8a3a 55%,#3b5c2a)"></div>
  <p>Lorem ipsum dolor sit amet, consectetur adipisicing elit, sed do eiusmod tempor incididunt ut labore et dolore.</p>
  <span class="card-arrow"><svg width="30" height="30"><path d="M13 10l5 5-5 5" fill="none" stroke="#fff" stroke-width="2"/></svg></span>
</article>
<article class="abs service-card" style="left:778px">
  <h3>TREE PRUNING</h3>
  <div class="service-photo" role="img" aria-label="Gloved hands pruning branches with loppers" style="background:linear-gradient(135deg,#4a6a2a,#7a9a4a 50%,#c0c8b0)"></div>
  <p>Lorem ipsum dolor sit amet, consectetur adipisicing elit, sed do eiusmod tempor incididunt ut labore et dolore.</p>
  <span class="card-arrow"><svg width="30" height="30"><path d="M13 10l5 5-5 5" fill="none" stroke="#fff" stroke-width="2"/></svg></span>
</article>
<a class="abs btn more-services">More services</a>

<section class="abs why" role="img" aria-label="Looking up into a green forest canopy"></section>
<div class="abs log-ring" role="img" aria-label="Cross-section of a cut log"></div>
<div class="abs why-disc">
  <div class="eyebrow center">Quillby Tree Care</div>
  <h2 class="section-title">WY <em>CHOOSE</em> US?</h2>
  <ul>
    <li>Licensed and Insured</li>
    <li>24-Hours Emergency Services</li>
    <li>Locally Owned &amp; Operated</li>
    <li>Professional Work</li>
    <li>Safety is Our No.1 Priority</li>
    <li>Free Estimates</li>
    <li>Licensed Arborist on Staff</li>
  </ul>
</div>

<section class="abs contact" role="img" aria-label="Misty forest background"></section>
<div class="abs contact-head">
  <div class="eyebrow center">Quillby Tree Care</div>
  <h2 class="section-title">GET IN <em>TOUCH</em></h2>
  <p>Consectetur adipisicing elit, sed do eiusmod tempor incididunt ut labore et dolore magna aliqua ut enim ad minim veniam.</p>
</div>
<div class="abs field" style="left:163px;top:2804px;width:278px;height:37px">Full Name:</div>
<div class="abs field" style="left:463px;top:2804px;width:276px;height:37px">Email Address:</div>
<div class="abs field" style="left:759px;top:2804px;width:278px;height:37px">Phone:</div>
<div class="abs field" style="left:163px;top:2861px;width:278px;height:37px">Subject:</div>
<div class="abs field" style="left:463px;top:2861px;width:574px;height:93px">Message...</div>
<div class="abs field" style="left:163px;top:2918px;width:278px;height:37px">Location:</div>
<a class="abs btn btn-solid submit">Submit now</a>

<footer class="abs site-footer"></footer>
<div class="abs footer-brand"><span class="brand-mark" style="width:40px;height:40px"></span><span class="brand-name">QUILLBY TREE CARE</span></div>
<p class="abs footer-about">At Quillby Tree Care, we are more than just a tree service company, we are stewards of our beautiful trees.</p>
<div class="abs quick-links">
  <div class="footer-h">Quick Links</div>
  <ul><li>Home</li><li>Who we are</li><li>Tree Care Services</li><li>Reviews</li><li>Contact Us</li></ul>
</div>
<div class="abs contact-info">
  <div class="footer-h">Contact Info</div>
  <div class="ci-row"><svg width="12" height="14" viewBox="0 0 12 14"><path d="M6 0a5 5 0 0 1 5 5c0 3.5-5 9-5 9S1 8.5 1 5a5 5 0 0 1 5-5z" fill="#f7a636"/><circle cx="6" cy="5" r="2" fill="#2e3a21"/></svg><span>1085 Lorem ipsum dolor it amet</span></div>
  <div class="ci-row"><svg width="12" height="12" viewBox="0 0 12 12"><path d="M2 1l2 0 1 3-1.5 1a7 7 0 0 0 3.5 3.5L8 7l3 1v2a1 1 0 0 1-1 1A9 9 0 0 1 1 2a1 1 0 0 1 1-1z" fill="#f7a636"/></svg><span>(337) 555-0148<br>(318) 555-0192</span></div>
  <div class="ci-row"><svg width="12" height="10" viewBox="0 0 12 10"><rect x="0" y="0" width="12" height="10" rx="1" fill="#f7a636"/><path d="M0 1l6 4 6-4" fill="none" stroke="#2e3a21" stroke-width="1"/></svg><span>info@quillbytreecare.com</span></div>
</div>
<div class="abs socials"><span></span><span class="on"></span><span></span></div>
<div class="abs locations footer-h">Our Locations</div>
<div class="abs map" role="img" aria-label="Map of service locations in New Mexico"></div>
<div class="abs copyright">Copyright © 2024 <b>QUILLBY</b> TREE CARE. All Rights Reserved</div>

</body>
</html>
```